Konzert
Zielgruppe
Chor bzw. Vocalensemble
Aufgabenstellung
Konzertplakat - Handzettel
Titel: Die Lerchenbund gibt ein Mordskonzert
Ort: Tettnang im Lindenhalle
Datum: 24.10.2015 20.00 Uhr
Es sollte auf jeden Fall erkennbar sein, dass es sich um ein Chorkonzert handelt.
Lieder sind alle zum Thema Verbrechen aber eher im zweideutigen Sinn.
Schon allein das Thema des Konzerts ist zweideutig zu verstehen.
Bei "Wibble Wobble" wird z.Bsp. eine Fliege in der Suppe gefunden...Ned Farrow wird einer erhängt, Moorwalzer zwielichtige Barszene, bei der "Kleinen Abend" erleidet jemand einen Gedächnisverlust, River bends versinnbildlich Blättersterben (Herbst).
Wir könnten uns aber auch ein "retromäßiges" Plakat vorstellen, im Stil Gangsterzeit wie sie gut zum Moorwalzer passt.
Wir werden Bilder anfügen, die eventuell auch nochmal überarbeitet werden müssen, weil sie ziemlich hell sind. Aber das können wir nach Auswahl noch machen. Die sind nicht zwingend einzusetzen, könnten aber mit eingebaut werden.
Wir sind offen für alles und sehr gespannt auf die Entwürfe.

```html
<!DOCTYPE html>
<html lang="de">
<head>
<meta charset="utf-8">
<title>Lerchenbund – Mordskonzert</title>
<link rel="stylesheet" href="https://fonts.googleapis.com/css2?family=Open+Sans:wght@700;800&family=Creepster&display=swap">
<style>
  :root {
    --page-bg: #e6e5e1;
    --paper: #ffffff;
    --ink: #111111;
    --accent-red: #d7111b;
    --note-grey-light: #d9d9d9;
    --note-grey-dark: #8a8a8a;
    --photo-light: #e9ecef;
    --photo-dark: #2a2a2c;
  }
  * { margin: 0; padding: 0; box-sizing: border-box; }
  html, body {
    width: 1200px; height: 1148px; overflow: hidden;
    background: var(--page-bg);
    font-family: "Open Sans", Arial, sans-serif;
  }
  .poster {
    position: absolute; left: 210px; top: 24px;
    width: 780px; height: 1100px;
    background: var(--paper);
    box-shadow: 0 2px 10px rgba(0,0,0,.12);
    overflow: hidden;
  }
  .title-pre {
    position: absolute; left: 92px; top: 28px;
    font-weight: 800; font-size: 60px; color: var(--ink); line-height: 1;
  }
  .title-name {
    position: absolute; left: 0; right: 0; top: 92px; text-align: center;
    font-weight: 800; font-size: 112px; letter-spacing: -2px;
    color: var(--ink); line-height: 1;
  }
  .note-strip {
    position: absolute; top: 250px; height: 640px; width: 132px;
    background: linear-gradient(180deg, var(--note-grey-light), var(--note-grey-dark) 45%, var(--note-grey-light) 70%, var(--note-grey-dark));
    opacity: .55;
  }
  .note-strip--left { left: 18px; }
  .note-strip--right { right: 18px; }
  .center-panel {
    position: absolute; left: 150px; top: 222px; width: 480px; height: 668px;
    background: var(--paper);
    box-shadow: 0 0 14px rgba(0,0,0,.18);
  }
  .choir-photo {
    position: absolute; left: 22px; top: 0; width: 436px; height: 300px;
    background: linear-gradient(180deg, var(--photo-light) 0%, #b9bcc0 35%, var(--photo-dark) 75%, #55585c 100%);
  }
  .photo-caption {
    position: absolute; left: 0; right: 0; top: 18px; text-align: center;
    font-weight: 800; font-size: 32px; color: var(--ink);
  }
  .badge {
    position: absolute; left: 535px; top: 435px;
    width: 156px; height: 156px; border-radius: 50%;
    background: var(--accent-red); border: 4px solid var(--paper);
    box-shadow: 0 2px 6px rgba(0,0,0,.25);
    color: var(--paper); text-align: center;
    display: flex; flex-direction: column; justify-content: center;
    line-height: 1.02;
  }
  .badge__big { font-weight: 800; font-size: 24px; }
  .badge__small { font-weight: 700; font-size: 12px; margin-top: 3px; line-height: 1.15; }
  .event-title {
    position: absolute; left: 0; right: 0; top: 560px; text-align: center;
    font-family: "Creepster", "Open Sans", cursive;
    font-size: 118px; line-height: 0.98; color: var(--accent-red);
  }
  .venue {
    position: absolute; left: 150px; width: 480px; top: 808px; text-align: center;
    font-weight: 800; font-size: 32px; line-height: 1.2; color: var(--ink);
  }
  .date-band {
    position: absolute; left: 40px; right: 40px; top: 890px; height: 190px;
    background: var(--accent-red); color: var(--paper); text-align: center;
    padding-top: 14px;
  }
  .date-band__date { font-weight: 800; font-size: 84px; line-height: 1; }
  .date-band__times { font-weight: 800; font-size: 32px; margin-top: 8px; line-height: 1.1; }
  .date-band__prices { font-weight: 800; font-size: 22px; margin-top: 10px; }
</style>
</head>
<body>
  <main class="poster">
    <div class="title-pre">Die</div>
    <h1 class="title-name">Lerchenbund</h1>

    <div class="note-strip note-strip--left" role="img" aria-label="Dekoratives Muster aus grauen Musiknoten"></div>
    <div class="note-strip note-strip--right" role="img" aria-label="Dekoratives Muster aus grauen Musiknoten"></div>

    <section class="center-panel">
      <div class="choir-photo" role="img" aria-label="Gruppenfoto des Chors in Schwarz mit bunten Federboas auf einer Treppe"></div>
      <div class="photo-caption">gibt ein</div>
    </section>

    <div class="badge">
      <span class="badge__big">Ein<br>CHOR-<br>KONZERT</span>
      <span class="badge__small">das unter<br>die Haut geht.</span>
    </div>

    <h2 class="event-title">Mords-<br>Konzert</h2>

    <p class="venue">Tettnang<br>im Lindenhalle</p>

    <section class="date-band">
      <div class="date-band__date">Sa., 24.10.2015</div>
      <div class="date-band__times">Einlass: 19.30 Uhr | Beginn: 20.00 Uhr</div>
      <div class="date-band__prices">Kartenvorverkauf: 15,– € | Abendkasse: 17,– €</div>
    </section>
  </main>
</body>
</html>
```